Business Carss for Harborlight Church

Need a progressive looking/modern business card design for my church

Target Market(s)

Families and young adults

Industry/Entity Type

Religious

Contact Information for Business Card

4728 Willow Crest Rd.
Frankfort Ky
502-318-4472

Rev. Tommy Fenwick
Slogan: Honor God and Make Discies

Font styles to use
Serif
Sans Serif
Decorative
Script

Colors
0555a3
3176b5

Requirements
Should not have
• Should not have a template look
• A unique out of the box look

```html
<!DOCTYPE html>
<html lang="en">
<head>
<meta charset="utf-8">
<title>Harborlight Church – Business Card</title>
<link rel="stylesheet" href="https://fonts.googleapis.com/css2?family=Cinzel:wght@500&family=Oswald:wght@400&family=PT+Sans:wght@400;700&display=swap">
<style>
  :root {
    --page-bg: #e9e7e4;
    --card-bg: #161616;
    --brand-blue: #0555a3;
    --accent-blue: #3176b5;
    --slogan-grey: #b9b9b9;
    --text-white: #ffffff;
  }
  * { margin: 0; padding: 0; box-sizing: border-box; }
  html, body {
    width: 1200px;
    height: 900px;
    overflow: hidden;
    background: var(--page-bg);
  }
  .business-card {
    position: absolute;
    left: 180px;
    top: 190px;
    width: 840px;
    height: 520px;
    background: var(--card-bg);
    border-radius: 260px 0 0 260px;
    box-shadow: 0 14px 40px rgba(0, 0, 0, 0.18);
  }
  .church-name {
    position: absolute;
    left: 94px;
    top: 210px;
    font-family: "Oswald", sans-serif;
    font-weight: 400;
    font-size: 42px;
    line-height: 1.2;
    letter-spacing: 1px;
    color: var(--brand-blue);
    text-transform: uppercase;
    white-space: nowrap;
  }
  .slogan {
    position: absolute;
    left: 94px;
    top: 322px;
    font-family: "Oswald", sans-serif;
    font-size: 23px;
    letter-spacing: 1.5px;
    color: var(--slogan-grey);
    text-transform: uppercase;
  }
  .pastor-name {
    position: absolute;
    right: 62px;
    top: 82px;
    font-family: "Cinzel", serif;
    font-weight: 500;
    font-size: 28px;
    color: var(--accent-blue);
    letter-spacing: 0.5px;
  }
  .contact {
    position: absolute;
    right: 62px;
    top: 280px;
    text-align: right;
    font-family: "PT Sans", sans-serif;
    font-size: 23px;
    line-height: 1.38;
    color: var(--text-white);
  }
  .contact__label {
    color: var(--accent-blue);
    font-weight: 700;
  }
  .contact__org {
    margin-top: 28px;
    color: var(--accent-blue);
    font-weight: 700;
    text-transform: uppercase;
  }
</style>
</head>
<body>
  <div class="business-card">
    <p class="church-name">Harborlight Church</p>
    <p class="slogan">Honor God and Make Discies</p>

    <p class="pastor-name">Rev. Tommy Fenwick</p>

    <div class="contact">
      <p class="contact__phone"><span class="contact__label">P:</span> 502-318-4472</p>
      <p class="contact__org">Harborlight Church</p>
      <p class="contact__street">4728 Willow Crest Rd.</p>
      <p class="contact__city">Frankfort Ky</p>
    </div>
  </div>
</body>
</html>
```